Awesome Professional Template for a collaborative report

File format: A4 PDF ideally

Design Requirements:

3 or 4 variants of a template some with graphics and pull quotes and a bio page for the essayists with a profile pic and a short descriptor

Layout Format: PPT would be perfect ideally portrait format

Style/Reference Guide: Varnholt or QP styles thought leadership reports as a guide

We need to input 10 essays around a specific subject with a nice layout with place holders for high impact pull quotes from the copy, stunning colourway and typrography probably A4 format but emailed as a PDF ideally not a huge file size. Striking front cover with title and list of contributors plus layout variations for the essays which will include a head shot short profile and contacts for the authors. Ideally a portrait format PPT that is easy to work with.

Target Market(s)

business professionals in brands

Industry/Entity Type

brand marketing

Font styles to use
Sans Serif

Colors
0054AA
0677BA
7BADD7
CADEEF
E8F1F8
00AB8E
00BBA5
67D7C9
C6EFE9
E9F9F6
F0912C
F2A743
F7CA91
FBE8D2
FDF5EE
6B429C
8869AF
B7A5CE
E3DAEB
F3F0F8

Requirements
Must have
• awesome visual impact

```html
<!DOCTYPE html>
<html lang="en">
<head>
<meta charset="utf-8">
<title>Predictive Analytics Report – Introduction &amp; Contents</title>
<link href="https://fonts.googleapis.com/css2?family=Poppins:wght@300;400;600;700&display=swap" rel="stylesheet">
<style>
  :root {
    --backdrop: #e2e2e2;
    --paper: #ffffff;
    --ink: #1c1c1c;
    --ink-soft: #5a5a5a;
    --purple: #8358b0;
    --teal: #2aa79b;
    --pink: #e83e8c;
    --orange: #e0882a;
    --quote-band: #dfe6ea;
  }
  * { margin: 0; padding: 0; box-sizing: border-box; }
  html, body {
    width: 1200px; height: 800px; overflow: hidden;
    background: var(--backdrop);
    font-family: "Poppins", sans-serif;
  }
  .spread {
    position: absolute; left: 180px; top: 103px;
    width: 840px; height: 594px;
    display: flex;
    box-shadow: 0 10px 30px rgba(0,0,0,0.15);
  }
  .page {
    position: relative; width: 420px; height: 594px;
    background: var(--paper); overflow: hidden;
  }
  .page--left { border-right: 1px solid #ececec; }

  .brand-tag {
    position: absolute; display: flex; align-items: center; gap: 4px;
    font-weight: 600; font-size: 10px; line-height: 12px; color: var(--teal); letter-spacing: 0.02em;
  }
  .brand-tag__dot { width: 8px; height: 8px; border-radius: 50%; background: var(--pink); }
  .page--left .brand-tag--top { top: 30px; right: 24px; }
  .page--left .brand-tag--bottom { bottom: 28px; left: 28px; }
  .page--right .brand-tag--top { top: 32px; right: 26px; }

  .page-title { position: absolute; left: 48px; font-weight: 700; font-size: 18px; line-height: 22px; }
  .intro__title { top: 48px; left: 53px; color: var(--purple); }
  .contents__title { top: 46px; left: 40px; color: var(--teal); }

  .intro__body {
    position: absolute; left: 53px; top: 88px;
    font-size: 11px; line-height: 13.7px; color: var(--ink); font-weight: 400;
  }
  .intro__body p + p { margin-top: 13.7px; }
  .intro__line { display: block; white-space: nowrap; }

  .toc { position: absolute; left: 40px; top: 84px; width: 323px; list-style: none; }
  .toc__item {
    display: flex; align-items: baseline; height: 20.3px;
    font-size: 10.5px; color: var(--ink-soft); font-weight: 300;
  }
  .toc__leader { flex: 1; border-bottom: 1px dotted #777; margin: 0 2px; transform: translateY(-3px); }
  .toc__page { color: var(--ink); }

  .quote-band {
    position: absolute; left: 0; right: 0; top: 385px; bottom: 0;
    background: var(--quote-band);
  }
  .pull-quote { position: absolute; left: 40px; top: 48px; }
  .pull-quote__mark {
    font-weight: 700; font-size: 30px; line-height: 18px; color: var(--orange);
  }
  .pull-quote__text {
    font-size: 13.3px; line-height: 17.6px; color: var(--orange); font-weight: 400;
    margin-top: 4px;
  }
  .pull-quote__line { display: block; white-space: nowrap; }
  .pull-quote__mark--close { display: inline-block; margin-left: 4px; vertical-align: -14px; }
  .pull-quote__author { font-size: 7.5px; color: var(--ink); margin-top: 2px; }
</style>
</head>
<body>
  <div class="spread">
    <section class="page page--left">
      <div class="brand-tag brand-tag--top"><span class="brand-tag__dot"></span>Quadra</div>
      <h1 class="page-title intro__title">Introduction</h1>
      <div class="intro__body">
        <p>
          <span class="intro__line">Over the last 5 decades, predictive analytics have</span>
          <span class="intro__line">become pivotal as a decision-making tool, but its initial</span>
          <span class="intro__line">conception reaches back much further. It all began back</span>
          <span class="intro__line">in 1689 with Aldwych’s of London insurance market. Whilst the</span>
          <span class="intro__line">processes were not as sophisticated and couldn’t quite</span>
          <span class="intro__line">predict as much as they can now, the original premise</span>
          <span class="intro__line">remains the same; Predictive analytics is a mathematical</span>
          <span class="intro__line">modelling tool that relies on historical data, data mining</span>
          <span class="intro__line">and machine learning to forecast outcomes.</span>
        </p>
        <p>
          <span class="intro__line">Here we explore 5 Predictive Analytics Techniques and</span>
          <span class="intro__line">Predictive Analytics Modelling and how these tools can</span>
          <span class="intro__line">be a highly effective way of compiling data into projected</span>
          <span class="intro__line">insights that can be implemented across your brand.</span>
        </p>
        <p>
          <span class="intro__line">There are hundreds of predictive analytics techniques</span>
          <span class="intro__line">that you can integrate with data for forecasting results.</span>
          <span class="intro__line">Here we explore 5 Predictive Analytics Techniques and</span>
          <span class="intro__line">Predictive Analytics Modelling and how these tools can</span>
          <span class="intro__line">be a highly effective way of compiling data into projected</span>
          <span class="intro__line">insights that can be implemented across your brand.</span>
        </p>
        <p>
          <span class="intro__line">There are hundreds of predictive analytics techniques</span>
          <span class="intro__line">that you can integrate with data for forecasting results.</span>
          <span class="intro__line">Here we explore 5 Predictive Analytics Techniques and</span>
          <span class="intro__line">Predictive Analytics Modelling and how these tools can</span>
          <span class="intro__line">be a highly effective way of compiling data into projected</span>
          <span class="intro__line">insights that can be implemented across your brand.</span>
        </p>
        <p>
          <span class="intro__line">There are hundreds of predictive analytics techniques</span>
          <span class="intro__line">that you can integrate with data for forecasting results.</span>
        </p>
      </div>
      <div class="brand-tag brand-tag--bottom"><span class="brand-tag__dot"></span>Quadra</div>
    </section>

    <section class="page page--right">
      <div class="brand-tag brand-tag--top"><span class="brand-tag__dot"></span>Quadra</div>
      <h2 class="page-title contents__title">Contents</h2>
      <ol class="toc">
        <li class="toc__item"><span>About the Authors</span><span class="toc__leader"></span><span class="toc__page">1</span></li>
        <li class="toc__item"><span>What is Predictive Analytics?</span><span class="toc__leader"></span><span class="toc__page">3</span></li>
        <li class="toc__item"><span>What is Predictive Analytics?</span><span class="toc__leader"></span><span class="toc__page">4</span></li>
        <li class="toc__item"><span>What is Predictive Analytics?</span><span class="toc__leader"></span><span class="toc__page">6</span></li>
        <li class="toc__item"><span>What is Predictive Analytics?</span><span class="toc__leader"></span><span class="toc__page">7</span></li>
        <li class="toc__item"><span>What is Predictive Analytics?</span><span class="toc__leader"></span><span class="toc__page">8</span></li>
        <li class="toc__item"><span>What is Predictive Analytics?</span><span class="toc__leader"></span><span class="toc__page">9</span></li>
        <li class="toc__item"><span>What is Predictive Analytics?</span><span class="toc__leader"></span><span class="toc__page">10</span></li>
        <li class="toc__item"><span>What is Predictive Analytics?</span><span class="toc__leader"></span><span class="toc__page">12</span></li>
        <li class="toc__item"><span>What is Predictive Analytics?</span><span class="toc__leader"></span><span class="toc__page">14</span></li>
        <li class="toc__item"><span>What is Predictive Analytics?</span><span class="toc__leader"></span><span class="toc__page">15</span></li>
        <li class="toc__item"><span>Citations</span><span class="toc__leader"></span><span class="toc__page">16</span></li>
      </ol>
      <div class="quote-band">
        <blockquote class="pull-quote">
          <div class="pull-quote__mark">“</div>
          <p class="pull-quote__text">
            <span class="pull-quote__line">We need to input 10 for high impact pull</span>
            <span class="pull-quote__line">quotes from the copy, stunning colourway and</span>
            <span class="pull-quote__line">typrography probably A4 format but emailed</span>
            <span class="pull-quote__line">cover with title and list of contributors plus layout</span>
            <span class="pull-quote__line">easy to work with.<span class="pull-quote__mark pull-quote__mark--close">”</span></span>
          </p>
          <p class="pull-quote__author">Tom Ashcroft</p>
        </blockquote>
      </div>
    </section>
  </div>
</body>
</html>
```